Zielgruppe
Friseurin für Damen und Herren
Aufgabenstellung
https://lumiraschnitt.de
Bitte erstelle mir anhand der Daten von der Website einen angepassten Entwurf mit Neueröffnung und geben keine Preise an sondern die kunden sollen sich direkt eingeladen führen um persönlich vor Ort vorbei zuschauen.

```html
<!DOCTYPE html>
<html lang="de">
<head>
<meta charset="utf-8">
<title>Große Eröffnung – Lumira Schnitt</title>
<link rel="stylesheet" href="https://fonts.googleapis.com/css2?family=Cinzel:wght@500;700;800&family=Great+Vibes&family=Figtree:wght@400;500&display=swap">
<style>
:root{
  --stage:#d9d9d9;
  --black:#050505;
  --gold:#d9a73a;
  --gold-light:#f2cc62;
  --gold-dark:#a87a22;
  --green:#5f7350;
  --rose:#e8b09c;
  --rose-line:#d99a86;
  --white:#ffffff;
  --ink:#111111;
}
*{margin:0;padding:0;box-sizing:border-box}
html,body{width:1200px;height:1117px;overflow:hidden;background:var(--stage)}
.poster{position:absolute;left:219px;top:20px;width:762px;height:1077px;background:var(--black);overflow:hidden;font-family:"Figtree",sans-serif;color:var(--white)}
.hero-photo{position:absolute;left:0;top:0;width:762px;height:470px;
  background:
    linear-gradient(180deg,rgba(5,5,5,0) 55%,var(--black) 100%),
    radial-gradient(ellipse at 42% 30%,#6a4a38 0%,#3a2d28 35%,transparent 65%),
    linear-gradient(90deg,#7a7876 0%,#4a4846 25%,#2a2a2e 55%,#3c3c42 80%,#2a2a2e 100%);}
.brand-tab{position:absolute;right:0;top:0;width:368px;height:116px}
.brand-name{position:absolute;right:0;top:0;width:330px;height:114px;display:flex;align-items:center;justify-content:center;
  font-family:"Cinzel",serif;font-weight:700;font-size:22px;letter-spacing:1px;color:var(--gold)}
.title-script{position:absolute;left:0;width:762px;top:268px;text-align:center;padding-left:20px;
  font-family:"Great Vibes",cursive;font-size:118px;line-height:1;color:var(--white)}
.title-main{position:absolute;left:0;width:762px;top:378px;text-align:center;
  font-family:"Cinzel",serif;font-weight:700;font-size:84px;line-height:1;
  background:linear-gradient(180deg,var(--gold-light) 0%,var(--gold) 50%,var(--gold-dark) 100%);
  -webkit-background-clip:text;background-clip:text;color:transparent}
.name-ribbon{position:absolute;left:102px;top:480px;width:559px;height:46px}
.name-ribbon span{position:absolute;inset:0;display:flex;align-items:center;justify-content:center;
  font-family:"Cinzel",serif;font-weight:700;font-size:27px;color:var(--white)}
.intro{position:absolute;left:100px;width:562px;top:538px;text-align:center;font-size:14.5px;line-height:1.3}
.divider{position:absolute;left:106px;top:604px;width:550px;height:14px}
.feature-title{position:absolute;left:0;width:762px;top:636px;text-align:center;
  font-family:"Cinzel",serif;font-weight:700;font-size:19px;color:var(--gold)}
.feature-copy{position:absolute;left:100px;width:562px;top:666px;text-align:center;font-size:12.6px;line-height:1.3}
.feature-copy p+p{margin-top:9px}
.quote-band{position:absolute;left:0;top:782px;width:762px;height:124px;background:var(--rose);
  display:flex;align-items:center;justify-content:center;padding:0 96px;text-align:center;
  font-family:"Cinzel",serif;font-weight:700;font-size:20.5px;line-height:1.1;color:var(--ink)}
.cta{position:absolute;left:0;top:906px;width:762px;height:89px;display:flex;align-items:center;justify-content:center;
  font-family:"Cinzel",serif;font-weight:800;font-size:40px;color:var(--white)}
.footer{position:absolute;left:0;top:995px;width:762px;height:82px;background:var(--green)}
.footer-web{position:absolute;left:0;top:0}
.social{position:absolute;left:86px;top:18px;height:38px;display:flex;align-items:center;gap:10px}
.social small{font-size:12.5px}
.social i{display:block;width:22px;height:22px;border-radius:50%;background:var(--white)}
.social b{font-family:"Cinzel",serif;font-weight:500;font-size:21px}
.website{position:absolute;left:490px;top:26px;width:262px;text-align:center;
  font-family:"Cinzel",serif;font-weight:700;font-size:22px;color:var(--gold)}
</style>
</head>
<body>
<main class="poster">
  <div class="hero-photo" role="img" aria-label="Foto: Friseurin frisiert eine Kundin im Salon mit Spiegeln und Lichtern"></div>

  <svg class="brand-tab" viewBox="0 0 368 116" aria-hidden="true">
    <path d="M0 0 H368 V114 H62 Q48 114 42 102 Z" fill="#050505" stroke="#d9a73a" stroke-width="2"/>
  </svg>
  <div class="brand-name">Lumira Schnitt</div>

  <div class="title-main">Eröffnung</div>
  <div class="title-script">Große</div>

  <div class="name-ribbon">
    <svg width="559" height="46" viewBox="0 0 559 46" aria-hidden="true">
      <path d="M10 0 H559 L545 23 L559 46 H0 L14 23 Z" fill="#5f7350"/>
    </svg>
    <span>Lumira Schnitt &amp; Beauty Lounge</span>
  </div>

  <p class="intro">Erleben Sie Schönheit und Stil in perfekter Harmonie. Unsere Experten verwandeln Ihre Träume in Realität.</p>

  <svg class="divider" viewBox="0 0 550 14" aria-hidden="true">
    <line x1="0" y1="7" x2="258" y2="7" stroke="#d99a86" stroke-width="1.5"/>
    <line x1="292" y1="7" x2="550" y2="7" stroke="#d99a86" stroke-width="1.5"/>
    <circle cx="275" cy="7" r="6" fill="none" stroke="#d99a86" stroke-width="1.5"/>
    <circle cx="275" cy="7" r="3" fill="#d99a86"/>
  </svg>

  <h2 class="feature-title">Moderne Ausstattung &amp; Wohlfühlatmosphäre</h2>
  <div class="feature-copy">
    <p>In unserem modernen Salon in Eschenwald erwarten Sie hochwertige Ausstattung und eine entspannte Atmosphäre. Unser erfahrenes Team sorgt dafür, dass Sie sich rundum wohlfühlen.</p>
    <p>Von klassischen Haarschnitten bis hin zu modernen Colorationen und Extensions - wir bieten Ihnen das komplette Spektrum der Friseurkunst auf höchstem Niveau.</p>
  </div>

  <blockquote class="quote-band">"Mehr als nur Haare. Wir schaffen Momente der Schönheit und des Wohlgefühls, die Ihre Persönlichkeit strahlen lassen – mit Herz, Hand und Leidenschaft."</blockquote>

  <div class="cta">Ihr neuer Look wartet</div>

  <footer class="footer">
    <svg class="footer-web" width="762" height="82" viewBox="0 0 762 82" aria-hidden="true">
      <path d="M762 12 H480 Q462 12 456 30 L448 60 Q442 82 420 82 H762 Z" fill="#ffffff"/>
    </svg>
    <div class="social"><small>Folgen Sie uns auf</small><i></i><b>@LUMIRA.SCHNITT</b></div>
    <div class="website">LUMIRASCHNITT.DE</div>
  </footer>
</main>
</body>
</html>
```